Semi completed website for an online chocolate shop to be completed

We have an existing logo and chocolate images. We want a modern, attractive and functional website. The aim is to sell our chocolate products so eCommerce is a must. Needs to be compatible with mobile devices. We need SEO optimisation and obviously want to get onto the first page for many searches. We specialise in vegan friendly chocolate, organic, etc.
Updates

Target Market(s)

People wanting to buy niche chocolates (vegan friendly, etc).

Industry/Entity Type

Chocolate Company

Coding

Coded - Design and coding required

Number of Pages Required

4 page

Font styles to use
Script

Colors
f68d4d
fee18a

Requirements
Must have
• The website must include attractive looking graphics, photos, and nice layout. The aim of the website is to Ecommerce and to provide a professional image for our brand, Velvet Cocoa.
Nice to have
• About Us, Shop, Home Page, Contact

```html
<!DOCTYPE html>
<html lang="en">
<head>
<meta charset="utf-8">
<title>Velvet Cocoa – Online Chocolate Shop</title>
<link href="https://fonts.googleapis.com/css2?family=Playfair+Display:ital,wght@0,700;1,700&family=Poppins:wght@400;500;600&display=swap" rel="stylesheet">
<style>
  :root{
    --page-bg:#e4ebef;
    --white:#ffffff;
    --green:#8cc152;
    --green-dark:#76a943;
    --brown:#5b504a;
    --brown-text:#4a3b33;
    --grey-text:#777777;
    --line:#e2e2e2;
    --accent-orange:#f68d4d;
    --accent-yellow:#fee18a;
  }
  *{box-sizing:border-box;margin:0;padding:0}
  html,body{width:1200px;height:900px;overflow:hidden}
  body{background:var(--page-bg);font-family:"Poppins",sans-serif;color:var(--brown-text);position:relative}

  .screen{position:absolute;background:var(--white);overflow:hidden;box-shadow:0 12px 40px rgba(60,80,90,.15)}

  /* ---------- desktop home page ---------- */
  .home{left:40px;top:110px;width:720px;height:640px}
  .hero{position:absolute;left:0;top:0;width:720px;height:410px;
    background:linear-gradient(110deg,#d9c3a6 0%,#c9a585 30%,#e8d7c6 55%,#b89478 78%,#8e7b5a 100%)}
  .hero-copy{position:absolute;left:0;right:0;top:120px;text-align:center;color:var(--white)}
  .hero-kicker{font-size:9px;letter-spacing:2px;text-transform:uppercase;font-weight:500}
  .hero-title{font-family:"Playfair Display",serif;font-style:italic;font-size:40px;margin:8px 0 12px}
  .btn-green{display:inline-block;background:var(--green);color:var(--white);font-size:9px;font-weight:600;
    text-transform:uppercase;letter-spacing:1px;padding:8px 18px;border-radius:16px}

  .header-bar{position:absolute;left:0;top:410px;width:720px;height:54px;background:var(--white)}
  .brand{position:absolute;left:46px;top:-30px;width:84px;height:84px;border-radius:50%;background:var(--white);
    border:2px solid var(--brown);display:flex;align-items:center;justify-content:center;
    font-weight:600;font-size:13px;color:var(--brown);text-align:center;line-height:1.1}
  .header-actions{position:absolute;right:24px;top:14px;display:flex;gap:10px;align-items:center}
  .call{font-size:12px;color:var(--green);font-weight:500;display:flex;align-items:center;gap:5px}
  .call b{color:var(--brown);font-weight:600}
  .pill{font-size:10px;padding:6px 14px;border-radius:14px;display:flex;align-items:center;gap:5px}
  .pill-account{background:var(--green);color:var(--white)}
  .pill-cart{border:1px solid var(--green);color:var(--brown)}

  .nav{position:absolute;left:0;top:464px;width:720px;height:32px;background:var(--brown);display:flex;align-items:center;padding-left:120px}
  .nav a{color:var(--white);font-size:9px;text-transform:uppercase;letter-spacing:1px;text-decoration:none;padding:0 20px;border-right:1px solid rgba(255,255,255,.3)}
  .nav a:last-of-type{border-right:none}
  .nav a.active{color:var(--green)}
  .search{position:absolute;right:0;top:0;width:240px;height:32px;background:var(--green);color:var(--white);
    font-size:10px;display:flex;align-items:center;justify-content:space-between;padding:0 14px}

  .intro-banner{position:absolute;left:40px;top:510px;width:460px;height:130px;
    background:linear-gradient(90deg,#9fdde0 0%,#8fd3d8 60%,#b48a62 100%)}
  .intro-copy{position:absolute;left:62px;top:548px}
  .intro-kicker{font-size:8px;letter-spacing:2px;text-transform:uppercase;color:var(--brown)}
  .intro-title{font-family:"Playfair Display",serif;font-size:26px;color:var(--brown-text);margin-top:6px}

  /* ---------- laptop favourites page ---------- */
  .shop{left:790px;top:250px;width:370px;height:440px;padding:20px 22px}
  .section-title{font-family:"Playfair Display",serif;font-size:15px;text-align:center;margin-bottom:14px}
  .cards{display:flex;gap:10px}
  .card{flex:1;text-align:center;border-bottom:2px solid var(--green)}
  .card-photo{height:104px}
  .card-body{padding:8px 4px;font-size:8px;line-height:1.3}
  .card-body .more{display:block;margin-top:6px;font-size:7px;color:var(--grey-text)}
  .card.featured .card-body{background:var(--green);color:var(--white)}
  .card.featured .more{color:var(--white)}
  .photo-a{background:linear-gradient(135deg,#7a5640,#3e2a1e)}
  .photo-b{background:linear-gradient(135deg,#c2a28a,#4a3020)}
  .photo-c{background:linear-gradient(135deg,#ece7e4,#6b4a36)}

  .promos{display:grid;grid-template-columns:1fr 1fr;gap:8px;margin-top:10px}
  .promo{position:relative;height:80px;background:#f3f1ef;overflow:hidden;padding:9px 10px}
  .promo-tall{grid-row:span 2;height:168px;background:linear-gradient(180deg,#f5f5f5,#dcdcdc)}
  .promo-kicker{font-size:7px;color:var(--accent-orange);text-transform:uppercase;font-weight:600;line-height:1.3}
  .promo-big{font-size:18px;font-weight:600;color:var(--brown-text)}
  .promo-name{font-size:10px;font-weight:500;color:var(--brown-text);line-height:1.35;white-space:nowrap}
  .promo-note{font-size:6px;color:var(--grey-text);margin-top:2px;width:78px;line-height:1.35}
  .btn-tiny{display:inline-block;background:var(--brown);color:var(--white);font-size:6px;padding:3px 7px;margin-top:4px;border-radius:2px}
  .promo-visual{position:absolute;right:6px;bottom:6px;width:56px;height:40px;border-radius:4px}
  .heart-visual{position:absolute;left:50px;bottom:10px;width:60px;height:54px;background:radial-gradient(circle,#e43a3a,#a91f1f);border-radius:8px}
  .truffle-visual{background:linear-gradient(135deg,#b08866,#4b2f20)}
  .gift-visual{background:linear-gradient(135deg,#f0e6d6,#b99a68)}
  .promo-tag{position:absolute;right:0;top:0;background:var(--accent-yellow);font-size:6px;padding:2px 6px}
</style>
</head>
<body>

  <!-- Home page -->
  <section class="screen home">
    <div class="hero" role="img" aria-label="Photo of a mother and daughter in bunny ears sharing chocolate"></div>
    <div class="hero-copy">
      <p class="hero-kicker">Rich and tasty chocolate</p>
      <h1 class="hero-title">Fresh Organic</h1>
      <span class="btn-green">Shop your favorite</span>
    </div>

    <header class="header-bar">
      <div class="brand">Velvet<br>Cocoa</div>
      <div class="header-actions">
        <span class="call">Call Us:
          <svg width="14" height="14" viewBox="0 0 24 24"><circle cx="12" cy="12" r="11" fill="none" stroke="#8cc152" stroke-width="2"/><path d="M8 7l2 0 1 3-1.5 1a7 7 0 0 0 3.5 3.5l1-1.5 3 1 0 2a2 2 0 0 1-2 2A9 9 0 0 1 6 9a2 2 0 0 1 2-2z" fill="#8cc152"/></svg>
          <b>123-555-0190</b></span>
        <span class="pill pill-account">
          <svg width="9" height="9" viewBox="0 0 10 10"><circle cx="5" cy="3" r="2.3" fill="#fff"/><path d="M0.5 10a4.5 4 0 0 1 9 0z" fill="#fff"/></svg>
          My Account</span>
        <span class="pill pill-cart">
          <svg width="10" height="10" viewBox="0 0 12 12"><path d="M0 1h2l2 7h6l1.5-5H3" fill="none" stroke="#5b504a" stroke-width="1.2"/><circle cx="5" cy="10.5" r="1" fill="#5b504a"/><circle cx="9" cy="10.5" r="1" fill="#5b504a"/></svg>
          My Cart $0.00</span>
      </div>
    </header>

    <nav class="nav">
      <a href="#" class="active">Home</a>
      <a href="#">About Us</a>
      <a href="#">Shop</a>
      <a href="#">Contact</a>
      <div class="search">Search here
        <svg width="11" height="11" viewBox="0 0 12 12"><circle cx="5" cy="5" r="3.8" fill="none" stroke="#fff" stroke-width="1.4"/><path d="M8 8l3 3" stroke="#fff" stroke-width="1.4"/></svg>
      </div>
    </nav>

    <div class="intro-banner" role="img" aria-label="Photo of a chocolate egg with sprinkles on a turquoise table"></div>
    <div class="intro-copy">
      <p class="intro-kicker">Velvet Cocoa</p>
      <h2 class="intro-title">Choose Our Treats</h2>
    </div>
  </section>

  <!-- Favourites page -->
  <section class="screen shop">
    <h2 class="section-title">Choose Your Favorite</h2>
    <div class="cards">
      <article class="card">
        <div class="card-photo photo-a" role="img" aria-label="Photo of chocolate gold collection bars"></div>
        <div class="card-body">Chocolate<br>Gold Collection<span class="more">Shop Now »</span></div>
      </article>
      <article class="card featured">
        <div class="card-photo photo-b" role="img" aria-label="Photo of assorted truffles"></div>
        <div class="card-body">Truffles<br>Chocolate<span class="more">Shop Now »</span></div>
      </article>
      <article class="card">
        <div class="card-photo photo-c" role="img" aria-label="Photo of a chocolate gift box"></div>
        <div class="card-body">Chocolate<br>Graduation Gifts<span class="more">Shop Now »</span></div>
      </article>
    </div>

    <div class="promos">
      <div class="promo promo-tall">
        <p class="promo-kicker">Save up to</p>
        <p class="promo-big">40% OFF</p>
        <p class="promo-name">Valentines Day<br>chocolate</p>
        <span class="btn-tiny">Shop Now</span>
        <div class="heart-visual" role="img" aria-label="Photo of a red heart chocolate"></div>
      </div>
      <div class="promo">
        <p class="promo-kicker">Save up to 20% off</p>
        <p class="promo-name">Delicious Choclate</p>
        <p class="promo-note">Smooth vegan cocoa in every bite</p>
        <span class="btn-tiny">Shop Now</span>
        <div class="promo-visual truffle-visual" role="img" aria-label="Photo of chocolate truffles"></div>
      </div>
      <div class="promo">
        <span class="promo-tag">Gift Ideas</span>
        <p class="promo-kicker">Save up to 30% off</p>
        <p class="promo-name">Birthday Treats</p>
        <div class="promo-visual gift-visual" role="img" aria-label="Photo of a wrapped chocolate gift"></div>
      </div>
    </div>
  </section>

</body>
</html>
```